Business Card Design

We are a contracting firm, 95% of my work is interior renovations.... but also don't want to preclude the idea of doing exterior work if it arises. I Need a business card that says I am the ultimate professional. There is a per-determined notion that all contractors are shady, unreliable, etc. Being that most of my work is in Manhattan, I would like to give the impression of fresh, modern, sleek, design/build firm.

Target Market(s)

young couples 25-40

Industry/Entity Type

Business

Contact Information for Business Card

PeterHollowayInteriors LLC
27 North Brandel Street
Marsh Hollow NY 11492
718-555-0142
646-555-0187- cell
www.phbwx.com
ph@phbwx.com
Peter Holloway

Requirements
Should not have
• do not want to give the impression of a "bargain basement store"

```html
<!DOCTYPE html>
<html lang="en">
<head>
<meta charset="utf-8">
<title>Peter Holloway – Business Card</title>
<link rel="stylesheet" href="https://fonts.googleapis.com/css2?family=Didact+Gothic&display=swap">
<style>
  :root {
    --card-bg: #ffffff;
    --brand-blue: #1a6db5;
    --web-grey: #555555;
    --body-ink: #111111;
    --mark-tint: #e6eff8;
    --mark-ring: #e4e4e4;
  }
  html, body {
    margin: 0;
    padding: 0;
    width: 1200px;
    height: 703px;
    overflow: hidden;
    background: var(--card-bg);
  }
  .card {
    position: relative;
    width: 1200px;
    height: 703px;
    background: var(--card-bg);
    font-family: "Didact Gothic", "Century Gothic", sans-serif;
    overflow: hidden;
  }
  .brand-mark {
    position: absolute;
    left: 400px;
    top: 150px;
    width: 460px;
    height: 320px;
    display: flex;
    align-items: center;
    gap: 16px;
    z-index: 0;
  }
  .brand-mark__dot {
    flex: none;
    width: 26px;
    height: 26px;
    border-radius: 50%;
    border: 3px solid var(--mark-ring);
  }
  .brand-mark__name {
    font-size: 40px;
    line-height: 1;
    color: var(--mark-tint);
    white-space: nowrap;
  }
  .holder-name {
    position: absolute;
    left: 62px;
    top: 78px;
    margin: 0;
    font-size: 81px;
    font-weight: 400;
    line-height: 1;
    color: var(--brand-blue);
    z-index: 1;
  }
  .website {
    position: absolute;
    right: 102px;
    top: 100px;
    font-size: 41px;
    line-height: 1;
    color: var(--web-grey);
    z-index: 1;
  }
  .contact {
    position: absolute;
    left: 72px;
    top: 456px;
    margin: 0;
    font-style: normal;
    font-size: 38px;
    line-height: 47.5px;
    color: var(--body-ink);
    z-index: 1;
  }
  .contact span { display: block; white-space: nowrap; }
  .contact .email { color: var(--brand-blue); }
</style>
</head>
<body>
  <main class="card">
    <div class="brand-mark">
      <span class="brand-mark__dot"></span>
      <span class="brand-mark__name">PeterHollowayInteriors</span>
    </div>

    <h1 class="holder-name">Peter Holloway</h1>
    <div class="website">www.phbwx.com</div>

    <address class="contact">
      <span class="company">PeterHollowayInteriors LLC</span>
      <span class="street">27 North Brandel Street Marsh Hollow NY 11492</span>
      <span class="phones">718-555-0142 646-555-0187- cell</span>
      <span class="email">ph@phbwx.com</span>
    </address>
  </main>
</body>
</html>
```